Multilingual Website for a Medico Company

We need a multilingual Website for our Medico company that sells gloves and masks, the website should have 3-5 subpages on 5 different languages.

Industry/Entity Type

Medtech

Number of Pages Required

5+ page

Requirements
Must have
• Unique Design - No template
Should not have
• No Templates

```html
<!DOCTYPE html>
<html lang="en">
<head>
<meta charset="utf-8">
<title>Curavia – Gloves &amp; Masks</title>
<link href="https://fonts.googleapis.com/css2?family=Lato:ital,wght@0,400;0,700;0,900;1,400&display=swap" rel="stylesheet">
<style>
:root{
  --green:#2f8a12;
  --green-dark:#1f6a0c;
  --green-bright:#4cae1f;
  --ink:#2b2b2b;
  --muted:#555;
  --topbar:#f2f2f2;
  --pink:#f7cde0;
  --grey-panel:#e8e8e8;
  --sky:#5bbfd8;
  --dark:#262626;
  --line:#d4d4d4;
}
*{margin:0;padding:0;box-sizing:border-box}
html,body{width:1200px;height:2862px;overflow:hidden}
body{font-family:'Lato',sans-serif;color:var(--ink);background:#fff;position:relative}
.abs{position:absolute}
.topbar{left:0;top:0;width:1200px;height:53px;background:var(--topbar);font-size:15px;font-weight:700}
.topbar .contact{left:74px;top:17px;display:flex;gap:14px;align-items:center}
.topbar .icons{right:74px;top:16px;display:flex;gap:26px;align-items:center;font-size:13px}
.header{top:53px;left:0;width:1200px;height:80px}
.brand{font-weight:900;color:var(--green);font-size:44px;letter-spacing:-1px;display:flex;align-items:center;gap:8px}
.brand .dot{width:16px;height:16px;background:var(--green);border-radius:50%}
.nav{right:68px;top:28px;display:flex;gap:36px;font-size:13px;font-weight:700;align-items:center}
.nav a{color:var(--ink);text-decoration:none;padding-bottom:6px}
.nav a.active{color:var(--green);border-bottom:2px solid var(--green)}
.cartbtn{width:28px;height:28px;border-radius:50%;background:var(--green-bright);display:inline-flex;align-items:center;justify-content:center}
.hero{top:133px;left:0;width:1200px;height:542px;background:var(--pink)}
.photo{display:block}
.hero-title{right:95px;top:160px;text-align:right}
.hero-title h1{font-size:50px;font-weight:900;font-style:italic;color:var(--green-dark);letter-spacing:1px}
.hero-title p{font-size:22px;font-style:italic;color:#333;line-height:28px;margin-top:6px}
.btn{background:var(--green);color:#fff;font-weight:700;display:inline-flex;align-items:center;justify-content:center;text-decoration:none}
.arrow{width:22px;height:40px}
.cat h2{font-weight:900;font-size:50px;position:absolute}
.section-title{top:962px;left:74px;width:1053px;text-align:center}
.section-title::before{content:"";position:absolute;left:0;right:0;top:20px;border-top:1px solid var(--line)}
.section-title span{position:relative;background:#fff;padding:0 15px;font-size:30px;font-weight:700}
.product{width:242px;text-align:center}
.product .thumb{height:219px;border:1px solid var(--line);display:flex;align-items:center;justify-content:center}
.product h3{font-size:15px;font-weight:700;margin-top:20px}
.product .desc{font-size:15px;color:var(--muted);margin-top:6px}
.product .price{font-size:17px;color:var(--green-dark);margin-top:12px}
.product .add{margin:12px auto 0;width:34px;height:34px;border-radius:50%;background:var(--green-bright);display:flex;align-items:center;justify-content:center}
h2.block{font-size:30px;font-weight:900;color:var(--ink)}
.copy{font-size:15px;line-height:29.5px;color:#333}
.tcard{left:615px;width:512px;background:#ececec;padding:18px 17px;clip-path:polygon(0 0,100% 0,100% 84%,0 100%)}
.tcard p{font-style:italic;font-size:14.5px;line-height:26px;color:#333}
.tcard h4{color:var(--green-dark);font-size:14px;font-weight:900;margin-top:8px}
.avatar{width:73px;height:73px}
.newsletter{top:2503px;left:0;width:1200px;height:119px;background:var(--dark)}
.footer h5{font-size:18px;font-weight:700}
.footer ul{list-style:none;font-size:13px;color:#444;line-height:28px;margin-top:6px}
.social{display:flex;gap:16px;margin-top:14px}
.social span{width:18px;height:18px;border-radius:50%;background:#555;display:block}
</style>
</head>
<body>

<div class="abs topbar">
  <div class="abs contact">
    <svg width="13" height="13" viewBox="0 0 24 24"><path fill="#2f8a12" d="M6.6 10.8a15 15 0 0 0 6.6 6.6l2.2-2.2a1 1 0 0 1 1-.25 11 11 0 0 0 3.6.6 1 1 0 0 1 1 1V20a1 1 0 0 1-1 1A17 17 0 0 1 3 4a1 1 0 0 1 1-1h3.5a1 1 0 0 1 1 1c0 1.25.2 2.45.6 3.6a1 1 0 0 1-.25 1z"/></svg>
    <span>1-800-555-0142</span><span style="font-weight:400">|</span>
    <svg width="15" height="12" viewBox="0 0 24 18"><rect width="24" height="18" rx="2" fill="#2f8a12"/><path d="M1 2l11 8 11-8" stroke="#fff" stroke-width="2" fill="none"/></svg>
    <span>hello@curavia-care.com</span>
  </div>
  <div class="abs icons">
    <svg width="15" height="15" viewBox="0 0 24 24"><circle cx="10" cy="10" r="7" stroke="#222" stroke-width="3" fill="none"/><path d="M15 15l6 6" stroke="#222" stroke-width="3"/></svg>
    <svg width="13" height="15" viewBox="0 0 20 24"><path d="M5 11V7a5 5 0 0 1 10 0v4" stroke="#222" stroke-width="3" fill="none"/><rect x="1" y="10" width="18" height="13" rx="2" fill="#222"/></svg>
    <svg width="15" height="15" viewBox="0 0 24 24"><circle cx="12" cy="7" r="5" fill="#222"/><path d="M2 23c0-6 4-9 10-9s10 3 10 9z" fill="#222"/></svg>
    <svg width="18" height="15" viewBox="0 0 24 21"><path d="M12 21L2 11A5.5 5.5 0 0 1 12 3a5.5 5.5 0 0 1 10 8z" fill="#222"/></svg>
    <span>EN &#8964;</span>
  </div>
</div>

<header class="abs header">
  <div class="abs brand" style="left:74px;top:10px">Curavia<span class="dot"></span></div>
  <nav class="abs nav">
    <a class="active" href="#">HOME</a><a href="#">GLOVES</a><a href="#">MASKS</a><a href="#">SHOP</a><a href="#">GIFTS</a><a href="#">BLOG</a><a href="#">CONTACT</a>
    <span style="display:flex;align-items:center;gap:8px;font-weight:400;font-size:12px;margin-left:-6px">
      <span class="cartbtn"><svg width="14" height="13" viewBox="0 0 24 22"><path d="M1 2h4l3 12h12l3-9H7" stroke="#fff" stroke-width="3" fill="none"/><circle cx="9" cy="19" r="2" fill="#fff"/><circle cx="19" cy="19" r="2" fill="#fff"/></svg></span>(0)
    </span>
  </nav>
</header>

<section class="abs hero">
  <div class="abs photo" role="img" aria-label="Woman in a blue surgical mask and purple gloves" style="left:0;top:0;width:560px;height:542px;background:linear-gradient(180deg,#f0d4c6 0%,#a3c8e6 45%,#7d74d8 80%,#c9c7d2 100%)"></div>
  <svg class="abs arrow" style="left:40px;top:200px" viewBox="0 0 22 40"><path d="M18 4L4 20l14 16" stroke="#fff" stroke-width="2.5" fill="none"/></svg>
  <svg class="abs arrow" style="right:40px;top:200px" viewBox="0 0 22 40"><path d="M4 4l14 16L4 36" stroke="#fff" stroke-width="2.5" fill="none"/></svg>
  <div class="abs hero-title">
    <h1>CURAVIA</h1>
    <p>I really want to make clothes that are feminine and<br>help women look beautiful.</p>
    <a class="btn" href="#" style="width:118px;height:37px;font-size:14px;margin-top:25px">SHOP NOW</a>
  </div>
</section>

<div class="abs cat" style="left:74px;top:597px;width:513px;height:319px">
  <div class="photo" role="img" aria-label="Hands pulling on blue nitrile gloves" style="width:100%;height:100%;background:linear-gradient(120deg,#2f8fd8 0%,#5f7384 55%,#3e4650 100%)"></div>
  <h2 style="right:26px;top:50px;color:#fff">GLOVES</h2>
</div>
<div class="abs cat" style="left:613px;top:597px;width:514px;height:319px">
  <div class="photo" role="img" aria-label="Blonde woman wearing a floral fabric mask" style="width:100%;height:100%;background:linear-gradient(90deg,#d8eef0 0%,#eaf4f5 45%,#e9d9b9 65%,#2d8fc6 80%,#a51d1d 100%)"></div>
  <h2 style="left:40px;top:130px;color:var(--green-dark)">MASKS</h2>
</div>

<div class="abs section-title"><span>FEATURED PRODUCTS</span></div>

<svg class="abs arrow" style="left:42px;top:1155px" viewBox="0 0 22 40"><path d="M16 6L4 20l12 14" stroke="#1f6a0c" stroke-width="2.5" fill="none"/></svg>
<svg class="abs arrow" style="right:42px;top:1155px" viewBox="0 0 22 40"><path d="M6 6l12 14L6 34" stroke="#1f6a0c" stroke-width="2.5" fill="none"/></svg>

<div class="abs product" style="left:74px;top:1040px">
  <div class="thumb"><div role="img" aria-label="Black fabric face mask" style="width:190px;height:135px;background:radial-gradient(ellipse at center,#222 55%,#fff 72%)"></div></div>
  <h3>PRODUCT NAME</h3><div class="desc">Duis aliquam nibh a dui</div><div class="price">$5.00</div>
  <div class="add"><svg width="14" height="13" viewBox="0 0 24 22"><path d="M1 2h4l3 12h12l3-9H7" stroke="#fff" stroke-width="3" fill="none"/><circle cx="9" cy="19" r="2" fill="#fff"/><circle cx="19" cy="19" r="2" fill="#fff"/></svg></div>
</div>
<div class="abs product" style="left:344px;top:1040px">
  <div class="thumb"><div role="img" aria-label="Pair of blue nitrile gloves" style="width:200px;height:140px;background:radial-gradient(ellipse at center,#1769e6 50%,#fff 72%)"></div></div>
  <h3>PRODUCT NAME</h3><div class="desc">Duis aliquam nibh a dui</div><div class="price">$5.00</div>
  <div class="add"><svg width="14" height="13" viewBox="0 0 24 22"><path d="M1 2h4l3 12h12l3-9H7" stroke="#fff" stroke-width="3" fill="none"/><circle cx="9" cy="19" r="2" fill="#fff"/><circle cx="19" cy="19" r="2" fill="#fff"/></svg></div>
</div>
<div class="abs product" style="left:614px;top:1040px">
  <div class="thumb"><div role="img" aria-label="Teal disposable surgical mask" style="width:210px;height:130px;background:radial-gradient(ellipse at center,#5fb0b8 50%,#fff 72%)"></div></div>
  <h3>PRODUCT NAME</h3><div class="desc">Duis aliquam nibh a dui</div><div class="price">$5.00</div>
  <div class="add"><svg width="14" height="13" viewBox="0 0 24 22"><path d="M1 2h4l3 12h12l3-9H7" stroke="#fff" stroke-width="3" fill="none"/><circle cx="9" cy="19" r="2" fill="#fff"/><circle cx="19" cy="19" r="2" fill="#fff"/></svg></div>
</div>
<div class="abs product" style="left:884px;top:1040px">
  <div class="thumb"><div role="img" aria-label="Pair of yellow rubber gloves" style="width:200px;height:140px;background:radial-gradient(ellipse at center,#f2b400 50%,#fff 72%)"></div></div>
  <h3>PRODUCT NAME</h3><div class="desc">Duis aliquam nibh a dui</div><div class="price">$5.00</div>
  <div class="add"><svg width="14" height="13" viewBox="0 0 24 22"><path d="M1 2h4l3 12h12l3-9H7" stroke="#fff" stroke-width="3" fill="none"/><circle cx="9" cy="19" r="2" fill="#fff"/><circle cx="19" cy="19" r="2" fill="#fff"/></svg></div>
</div>

<section class="abs" style="left:0;top:1450px;width:613px;height:438px;background:var(--grey-panel)">
  <h2 class="block abs" style="left:75px;top:64px">WELCOME TO CURAVIA</h2>
  <p class="copy abs" style="left:75px;top:113px;width:500px">Lorem ipsum dolor sit amet, consectetur adipiscing elit. Donec non dui aliquet lacus interdum finibus ac non sem. Aenean non leo mauris. Mauris ligula mauris, congue id turpis vel, tristique sollicitudin lacus.<br>Sed eget finibus risus. Cras lacinia diam nunc, vitae auctor risus bibendum nec. Ut id velit vitae felis gravida suscipit eget et libero. Morbi eget congue risus. Morbi porta pellentesque feugiat.</p>
  <a class="btn abs" href="#" style="left:75px;top:320px;width:151px;height:50px;font-size:15px">READ MORE</a>
</section>
<div class="abs photo" role="img" aria-label="Surgical mask and blue gloves on a turquoise background" style="left:613px;top:1450px;width:587px;height:438px;background:radial-gradient(ellipse at 55% 50%,#3f7fe0 0%,#5fc2dc 55%,#5bbfd8 100%)"></div>

<h2 class="block abs" style="left:75px;top:1944px">WHY CHOOSE US?</h2>
<div class="abs photo" role="img" aria-label="Woman in mask making a heart shape with gloved hands" style="left:74px;top:1999px;width:513px;height:235px;background:linear-gradient(90deg,#dcd6cc 0%,#7fb3b4 30%,#c29a82 50%,#7fb3b4 70%,#d9d3c8 100%)"></div>
<p class="copy abs" style="left:75px;top:2252px;width:500px">Lorem ipsum dolor sit amet, consectetur adipiscing elit. Donec non dui aliquet lacus interdum finibus ac non sem. Aenean non leo mauris. Mauris ligula mauris, congue id turpis vel, tristique sollicitudin lacus. Sed eget finibus risus.</p>
<a class="btn abs" href="#" style="left:75px;top:2390px;width:151px;height:50px;font-size:15px">READ MORE</a>

<h2 class="block abs" style="left:615px;top:1944px">TESTIMONIALS</h2>
<svg class="abs" style="left:1085px;top:1948px" width="14" height="24" viewBox="0 0 14 24"><path d="M11 3L3 12l8 9" stroke="#222" stroke-width="2" fill="none"/></svg>
<svg class="abs" style="left:1113px;top:1948px" width="14" height="24" viewBox="0 0 14 24"><path d="M3 3l8 9-8 9" stroke="#222" stroke-width="2" fill="none"/></svg>

<div class="abs tcard" style="top:1999px;height:162px">
  <p>“ Lorem ipsum dolor sit amet, consectetur adipiscing elit onec non dui aliquet lacus interdum finibus ac non sem. Aenean non leo mauris. Mauris ligula mauris, congue id turpis vel..</p>
  <h4>NAME HEADING</h4>
</div>
<div class="abs photo avatar" role="img" aria-label="Portrait of a customer in a mask" style="left:645px;top:2134px;background:linear-gradient(180deg,#b9c6d2,#6cb2e0 60%,#e8eef3)"></div>

<div class="abs tcard" style="top:2231px;height:160px">
  <p>“ Lorem ipsum dolor sit amet, consectetur adipiscing elit onec non dui aliquet lacus interdum finibus ac non sem. Aenean non leo mauris. Mauris ligula mauris, congue id turpis vel..</p>
  <h4>NAME HEADING</h4>
</div>
<div class="abs photo avatar" role="img" aria-label="Portrait of a customer in a mask" style="left:645px;top:2368px;background:linear-gradient(180deg,#8c8c8c,#d9c3b3 50%,#c75a5a)"></div>

<section class="abs newsletter">
  <div class="abs" style="left:238px;top:40px;color:#fff;font-size:28px;font-weight:700">NEWSLETTER SIGN UP</div>
  <div class="abs" style="left:572px;top:36px;width:328px;height:47px;background:#fff;font-size:12px;color:#444;padding:17px 14px">ENTER EMAIL ADDRESS</div>
  <div class="abs btn" style="left:900px;top:36px;width:60px;height:47px;background:var(--green-bright);font-size:16px;font-weight:900">GO</div>
</section>

<footer class="abs footer" style="left:0;top:2622px;width:1200px;height:240px">
  <div class="abs brand" style="left:74px;top:42px;font-size:36px">Curavia<span class="dot" style="width:13px;height:13px"></span></div>
  <div class="abs" style="left:75px;top:128px;font-size:12px;line-height:22px;color:#333">Copyright © 2020. Company Name.<br>All Right Reserved</div>
  <div class="abs" style="left:361px;top:46px">
    <h5>NAVIGATION</h5>
    <div style="display:flex;gap:48px"><ul><li>Home</li><li>Gloves</li><li>Masks</li><li>Shop</li></ul><ul><li>Gifts</li><li>Blog</li><li>Contact</li></ul></div>
  </div>
  <div class="abs" style="left:612px;top:46px">
    <h5>MY ACCOUNT</h5>
    <ul><li>Vestibulum ante</li><li>Ipsum primis</li><li>Faucibus orci luctus</li><li>Ultrices posuere</li><li>Cubilia</li></ul>
  </div>
  <div class="abs" style="left:843px;top:46px">
    <h5>FOLLOW US</h5>
    <div class="social"><span></span><span></span><span></span><span></span><span></span></div>
  </div>
</footer>

</body>
</html>
```